International Property Consultancy

Brief Overview:

I need a dynamic and well designed website that is easy to use and understand. It has to be unique and different to generic templates that most websites seem to be these days. PLEASE NO GENERIC TEMPLATES FROM THE INTERNET.

Our business has 10 years experience working on struggling international developments that we then work in-house for to turn around and brings bout success. We stay within a project often for long periods of time until success is achieved. We are unique in our approach and completely different to the standard routes to market for many developments. The site is for developers to see what we have done in regards to previous projects, as such we want to incorporate video into this site with a strong design aesthetic. There will be videos of the past projects we have worked on, which will act as case studies.

I like very simple but punchy websites, that people can navigate and understand very easily. Also a big fan of unique and well thought out design aesthetic.

Initial Site layout thoughts:

1) Homepage:
2) About Us
3) What we've done / Work
This part has the projects we have worked on (France, Portugal, London, Morocco). Each one will have some video content and photo images, but also would be good to have a succinct way to mention what we did and the successes in a clever and punchy way.

4) Contact Us

* This is just a guideline. Would be open to input and creative direction on your own part.

*More details and websites we like can be seen in the brief doc attached.

PLEASE VIEW THE WIREFRAME WORD DOC ATTACHED.

Here there are also some more examples to help:

Here are just a few examples of websites and what I like about them:

- www.velmoro.com (clean, nice geometric design aesthetic, good animation when loading and changing pages well thought out all though also coulee be considered a bit dull and basic after the initial homepage slide)
- https://www.farbridgehub.net (Clean site, quite clinical, lacks video content and doesn't engage greatly).
- https://ruskotile.com (minimal, and like how it mixes the design aesthetic more with video and photo content)

- https://www.amberquillworks.com (like the layout of this and how it displays the projects and work section)

- https://brisk.com (Good use of video content)

- https://loomfield.studio (minimal to the point and mixes design with video and animation etc...)

Here is another couple of cool websites that may help give you some direction: https://halvenquay.com www.brisk.com

Hi there, One of the things I thought would be good on the homepage is to add the logo with a 'digital landscape' before flicking down into a slide with video content of the projects... Just an idea but have posted some pics in the brief. We would get this animated for the site. But if you have better ideas, please do run with them. Thanks,

Target Market(s)

Property developers

Number of Pages Required

4 page

Font styles to use
Other font styles liked:
• Read brief

Requirements
Must have
• Needs to be clean, dynamic and easy to follow on desktop and mobile. We will use it as a kind of portfolio website so will need to embed video of past projects we have worked on.

Read brief in docs.
Nice to have
• Clean
Should not have
• Not be another generic template website.
Not have random property stock photos. (We are not a property agency).

```html
<!DOCTYPE html>
<html lang="en">
<head>
<meta charset="utf-8">
<title>Calvanta — International Property Consultancy</title>
<link href="https://fonts.googleapis.com/css2?family=Baloo+2:wght@400;500;600;700&display=swap" rel="stylesheet">
<style>
:root{
  --ink:#111;
  --text:#333;
  --muted:#666;
  --band:#f9f9f9;
  --arc:#efefef;
  --line:#d8d8d8;
  --white:#fff;
}
*{box-sizing:border-box;margin:0;padding:0}
html,body{width:1200px;height:2963px;overflow:hidden}
body{position:relative;background:var(--white);font-family:'Baloo 2',sans-serif;color:var(--text)}
.abs{position:absolute}
.brand{font-size:30px;font-weight:500;color:var(--ink);letter-spacing:-.5px;line-height:1}
.nav{top:22px;left:758px;display:flex;gap:32px;font-size:12px;color:var(--ink)}
.nav a{color:inherit;text-decoration:none;position:relative}
.nav a.active::after{content:"";position:absolute;left:50%;bottom:-7px;width:16px;height:2px;margin-left:-8px;background:var(--ink)}
.social{display:flex;gap:10px}
.social span{width:14px;height:14px;border-radius:50%;background:var(--ink);display:block}
.hero-intro{left:104px;top:226px;width:420px}
.hero-intro .pre{font-size:20px;color:var(--ink);line-height:1.2}
.hero-intro h1{font-size:29px;font-weight:700;color:var(--ink);line-height:1.3;margin-top:4px}
.hero-intro p{font-size:13px;color:var(--muted);line-height:1.35;margin-top:8px}
.scroll{left:61px;top:524px;font-size:12px;color:var(--muted);display:flex;align-items:center;gap:6px}
.about{top:563px;left:0;width:1200px;height:359px;background:var(--band);text-align:center}
.section-title{font-size:19px;font-weight:700;color:var(--ink);letter-spacing:.3px;position:relative;display:inline-block}
.section-title::after{content:"";position:absolute;left:50%;bottom:-3px;width:30px;height:2px;margin-left:-15px;background:var(--ink)}
.about .section-title{margin-top:68px}
.about .lead{font-size:19px;color:var(--ink);line-height:1.25;margin:32px auto 0;width:620px}
.about .body{font-size:12px;color:var(--ink);line-height:1.6;margin:18px auto 0;width:780px}
.btn{display:inline-flex;align-items:center;justify-content:center;gap:8px;width:108px;height:27px;border:1px solid var(--line);border-radius:14px;font-size:11px;color:var(--ink);background:var(--white)}
.about .btn{margin-top:22px}
.projects-title{top:978px;left:0;width:1200px;text-align:center}
.project{width:420px}
.project h2{font-size:21px;font-weight:600;color:var(--ink);letter-spacing:.3px;line-height:1.2}
.project .desc{font-size:11px;color:var(--text);line-height:1.5;margin-top:8px;width:330px}
.features{display:grid;grid-template-columns:204px 200px;row-gap:14px;margin-top:20px}
.feature{display:flex;align-items:center;gap:12px;font-size:10.5px;font-weight:600;color:var(--ink);line-height:1.3;height:34px}
.feature svg{flex:none}
.project .btn{margin-top:30px}
.visual{overflow:hidden}
.play{width:58px;height:58px}
.footer-bg{top:2620px;left:0;width:1200px;height:343px}
.footer-brand{top:2680px;left:0;width:1200px;text-align:center}
.tagline{top:2721px;left:0;width:1200px;text-align:center;font-size:14px;color:var(--text)}
.contact-card{top:2783px;left:214px;width:770px;height:81px;background:var(--white);box-shadow:0 2px 14px rgba(0,0,0,.06);display:flex;align-items:center;font-size:11px;color:var(--ink)}
.contact-item{display:flex;align-items:center;gap:12px}
.contact-stack{display:flex;flex-direction:column;align-items:center;gap:6px}
.divider{width:1px;height:36px;background:var(--line)}
.footer-nav{top:2891px;left:0;width:1200px;display:flex;justify-content:center;gap:20px;font-size:11px;color:var(--ink)}
.footer-nav i{font-style:normal;color:var(--muted)}
.copyright{top:2917px;left:0;width:1200px;text-align:center;font-size:10px;color:var(--muted)}
</style>
</head>
<body>

<svg width="0" height="0" style="position:absolute">
  <defs>
    <symbol id="play" viewBox="0 0 58 58"><circle cx="29" cy="29" r="29" fill="#111"/><path d="M22 17 L41 29 L22 41 Z" fill="none" stroke="#fff" stroke-width="2.4" stroke-linejoin="round"/></symbol>
    <symbol id="ic-bulb" viewBox="0 0 28 28" fill="none" stroke="#111" stroke-width="1.3"><circle cx="14" cy="12" r="6"/><path d="M11 18v4h6v-4M14 2v2M4 12h2M22 12h2M7 5l1.5 1.5M21 5l-1.5 1.5"/></symbol>
    <symbol id="ic-crane" viewBox="0 0 28 28" fill="none" stroke="#111" stroke-width="1.3"><rect x="3" y="14" width="14" height="8" rx="1"/><path d="M10 14 L22 3 L25 6 L15 14M5 25h11"/><circle cx="6" cy="25" r="1.5"/><circle cx="14" cy="25" r="1.5"/></symbol>
    <symbol id="ic-team" viewBox="0 0 28 28" fill="none" stroke="#111" stroke-width="1.3"><circle cx="14" cy="9" r="3"/><circle cx="6" cy="12" r="2.5"/><circle cx="22" cy="12" r="2.5"/><path d="M8 24v-4a6 6 0 0 1 12 0v4M1 24v-3a5 5 0 0 1 6-4M27 24v-3a5 5 0 0 0-6-4"/></symbol>
    <symbol id="ic-arch" viewBox="0 0 28 28" fill="none" stroke="#111" stroke-width="1.3"><path d="M3 6 L25 10 L22 24 L2 20 Z"/><path d="M8 12 L8 18 L14 19 Z"/></symbol>
    <symbol id="arrow" viewBox="0 0 12 12" fill="none" stroke="#111" stroke-width="1.5"><path d="M1 6h9M6 2l4 4-4 4"/></symbol>
  </defs>
</svg>

<!-- Header -->
<div class="abs brand" style="left:61px;top:16px">Calvanta.</div>
<nav class="abs nav">
  <a class="active">Home</a><a>About Us</a><a>Work</a><a>Contact Us</a>
</nav>
<div class="abs social" style="left:1076px;top:23px"><span></span><span></span><span></span></div>

<!-- Hero -->
<svg class="abs" style="left:600px;top:60px" width="600" height="503" viewBox="0 0 600 503">
  <defs>
    <linearGradient id="g-hero" x1="0" y1="0" x2="1" y2="1"><stop offset="0" stop-color="#f6f6f6"/><stop offset="1" stop-color="#dedede"/></linearGradient>
    <clipPath id="c-hero"><rect width="600" height="503"/></clipPath>
  </defs>
  <g clip-path="url(#c-hero)">
    <ellipse cx="480" cy="330" rx="470" ry="440" fill="var(--arc)"/>
    <ellipse cx="520" cy="330" rx="460" ry="450" fill="#fff"/>
    <path role="img" aria-label="Pale upward view of a white stepped high-rise facade" d="M520 0 L600 0 L600 503 L120 503 C60 420 60 200 200 80 C280 20 400 0 520 0 Z" fill="url(#g-hero)"/>
  </g>
  <use href="#play" x="62" y="214" width="58" height="58"/>
</svg>
<div class="abs hero-intro">
  <div class="pre">Our business has</div>
  <h1>10 years’ experience working</h1>
  <p>on struggling international developments that we then work in-house for to turn around and brings bout success.</p>
</div>
<div class="abs scroll">Scroll to explore <svg width="10" height="12" viewBox="0 0 10 12" fill="none" stroke="#111" stroke-width="1.5"><path d="M5 1v9M1 6l4 4 4-4"/></svg></div>

<!-- About -->
<section class="abs about">
  <h2 class="section-title">ABOUT US</h2>
  <p class="lead">Calvanta is a consultancy company that helps international property developments fulfil their potential.</p>
  <p class="body">The company has had great success over the last <b>10 YEARS</b> of turning around struggling property developments (often resort and investment) and making them reach their maximum potential. We have completed projects in Portugal, London, France, Morocco, Brazil etc...</p>
  <span class="btn">Read More <svg width="10" height="10"><use href="#arrow"/></svg></span>
</section>

<!-- Projects -->
<div class="abs projects-title"><h2 class="section-title">OUR UNIQUE PROJECTS</h2></div>

<!-- Portugal -->
<svg class="abs visual" style="left:600px;top:1050px" width="600" height="340" viewBox="0 0 600 340">
  <defs><linearGradient id="g-pt" x1="0" y1="0" x2="0" y2="1"><stop offset="0" stop-color="#5d8fd6"/><stop offset=".55" stop-color="#c9d6e4"/><stop offset="1" stop-color="#29b3e0"/></linearGradient></defs>
  <path d="M460 0 C240 10 0 150 50 300 C60 325 80 340 90 340 L600 340 L600 60 C560 20 520 0 460 0 Z" fill="var(--arc)"/>
  <path role="img" aria-label="Resort villa with arched doorway beside a blue pool and mountains" d="M440 0 C560 0 600 60 600 60 L600 340 L100 340 C60 270 60 170 150 110 C240 45 330 0 440 0 Z" fill="url(#g-pt)"/>
  <use href="#play" x="69" y="165" width="58" height="58"/>
</svg>
<div class="abs project" style="left:181px;top:1104px">
  <h2>Portugal Resort</h2>
  <p class="desc">Lorem Ipsum is simply dummy text of the printing and typesetting industry. Lorem Ipsum has been the industry’s standard dummy text ever...</p>
  <div class="features">
    <div class="feature"><svg width="28" height="28"><use href="#ic-bulb"/></svg>Unique way of Project<br>Planning</div>
    <div class="feature"><svg width="28" height="28"><use href="#ic-crane"/></svg>Efficient Machines &amp; Men<br>behind project</div>
    <div class="feature"><svg width="28" height="28"><use href="#ic-team"/></svg>Expert Efforts from<br>Experienced Team</div>
    <div class="feature"><svg width="28" height="28"><use href="#ic-arch"/></svg>Professional Architect</div>
  </div>
  <span class="btn">Read More <svg width="10" height="10"><use href="#arrow"/></svg></span>
</div>

<!-- Morocco -->
<svg class="abs visual" style="left:0;top:1438px" width="560" height="342" viewBox="0 0 560 342">
  <defs><linearGradient id="g-ma" x1="0" y1="0" x2="1" y2="1"><stop offset="0" stop-color="#e8e8e8"/><stop offset="1" stop-color="#bdbdbd"/></linearGradient></defs>
  <path d="M200 2 C380 40 560 140 555 220 C550 300 500 340 470 342 L0 342 L0 0 Z" fill="var(--arc)"/>
  <path d="M190 10 C360 50 520 140 515 220 C510 300 470 340 440 342 L0 342 L0 10 Z" fill="#fff"/>
  <path role="img" aria-label="Curved white high-rise with horizontal bands of windows" d="M100 30 C200 20 300 60 400 120 C470 165 490 250 440 342 L85 342 C70 250 70 120 100 30 Z" fill="url(#g-ma)"/>
  <use href="#play" x="471" y="167" width="58" height="58"/>
</svg>
<div class="abs project" style="left:647px;top:1493px">
  <h2>Morocco</h2>
  <p class="desc">Lorem Ipsum is simply dummy text of the printing and typesetting industry. Lorem Ipsum has been the industry’s standard dummy text ever...</p>
  <div class="features">
    <div class="feature"><svg width="28" height="28"><use href="#ic-bulb"/></svg>Unique way of Project<br>Planning</div>
    <div class="feature"><svg width="28" height="28"><use href="#ic-crane"/></svg>Efficient Machines &amp; Men<br>behind project</div>
    <div class="feature"><svg width="28" height="28"><use href="#ic-team"/></svg>Expert Efforts from<br>Experienced Team</div>
    <div class="feature"><svg width="28" height="28"><use href="#ic-arch"/></svg>Professional Architect</div>
  </div>
  <span class="btn">Read More <svg width="10" height="10"><use href="#arrow"/></svg></span>
</div>
<div class="abs" style="left:0;top:1779px;width:1200px;height:1px;background:#f1f1f1"></div>

<!-- London -->
<svg class="abs visual" style="left:640px;top:1835px" width="560" height="340" viewBox="0 0 560 340">
  <defs><linearGradient id="g-ld" x1="0" y1="0" x2="1" y2="1"><stop offset="0" stop-color="#f0f0f0"/><stop offset="1" stop-color="#b8b8b8"/></linearGradient></defs>
  <path d="M400 0 C200 20 0 120 5 220 C10 300 60 340 80 340 L560 340 L560 0 Z" fill="var(--arc)"/>
  <path d="M420 8 C230 30 45 130 50 220 C55 300 100 340 120 340 L560 340 L560 8 Z" fill="#fff"/>
  <path role="img" aria-label="Rounded white office tower with curved glass bands" d="M300 60 C330 20 370 20 380 60 L460 200 C480 260 480 300 470 340 L180 340 C175 260 200 180 260 120 Z" fill="url(#g-ld)"/>
  <use href="#play" x="29" y="166" width="58" height="58"/>
</svg>
<div class="abs project" style="left:181px;top:1889px">
  <h2>London</h2>
  <p class="desc">Lorem Ipsum is simply dummy text of the printing and typesetting industry. Lorem Ipsum has been the industry’s standard dummy text ever...</p>
  <div class="features">
    <div class="feature"><svg width="28" height="28"><use href="#ic-bulb"/></svg>Unique way of Project<br>Planning</div>
    <div class="feature"><svg width="28" height="28"><use href="#ic-crane"/></svg>Efficient Machines &amp; Men<br>behind project</div>
    <div class="feature"><svg width="28" height="28"><use href="#ic-team"/></svg>Expert Efforts from<br>Experienced Team</div>
    <div class="feature"><svg width="28" height="28"><use href="#ic-arch"/></svg>Professional Architect</div>
  </div>
  <span class="btn">Read More <svg width="10" height="10"><use href="#arrow"/></svg></span>
</div>
<div class="abs" style="left:0;top:2174px;width:1200px;height:1px;background:#f1f1f1"></div>

<!-- France -->
<svg class="abs visual" style="left:0;top:2226px" width="560" height="340" viewBox="0 0 560 340">
  <defs><linearGradient id="g-fr" x1="0" y1="0" x2="1" y2="1"><stop offset="0" stop-color="#f2f2f2"/><stop offset="1" stop-color="#9a9a9a"/></linearGradient></defs>
  <path d="M220 0 C400 50 560 150 555 230 C550 300 510 340 480 340 L0 340 L0 0 Z" fill="var(--arc)"/>
  <path d="M210 8 C380 60 520 150 515 230 C510 300 480 340 450 340 L0 340 L0 8 Z" fill="#fff"/>
  <path role="img" aria-label="Modern building with a white lattice dome over banded facade" d="M190 20 C300 40 420 110 500 200 C520 260 500 310 470 340 L0 340 L0 190 C60 150 130 130 170 120 C175 80 180 50 190 20 Z" fill="url(#g-fr)"/>
  <use href="#play" x="471" y="165" width="58" height="58"/>
</svg>
<div class="abs project" style="left:647px;top:2279px">
  <h2>France</h2>
  <p class="desc">Lorem Ipsum is simply dummy text of the printing and typesetting industry. Lorem Ipsum has been the industry’s standard dummy text ever...</p>
  <div class="features">
    <div class="feature"><svg width="28" height="28"><use href="#ic-bulb"/></svg>Unique way of Project<br>Planning</div>
    <div class="feature"><svg width="28" height="28"><use href="#ic-crane"/></svg>Efficient Machines &amp; Men<br>behind project</div>
    <div class="feature"><svg width="28" height="28"><use href="#ic-team"/></svg>Expert Efforts from<br>Experienced Team</div>
    <div class="feature"><svg width="28" height="28"><use href="#ic-arch"/></svg>Professional Architect</div>
  </div>
  <span class="btn">Read More <svg width="10" height="10"><use href="#arrow"/></svg></span>
</div>

<!-- Footer -->
<svg class="abs footer-bg" width="1200" height="343" viewBox="0 0 1200 343">
  <defs><linearGradient id="g-ft" x1="0" y1="0" x2="1" y2="0"><stop offset="0" stop-color="#fff"/><stop offset="1" stop-color="#f1f1f1"/></linearGradient></defs>
  <rect role="img" aria-label="Faint white high-rise facade behind the footer" x="780" y="0" width="420" height="343" fill="url(#g-ft)"/>
</svg>
<div class="abs footer-brand"><span class="brand">Calvanta.</span></div>
<div class="abs tagline">A special and qualified service dedicated to luxury properties</div>
<div class="abs contact-card">
  <div class="contact-item" style="margin-left:64px;width:190px">
    <svg width="14" height="18" viewBox="0 0 14 18" fill="none" stroke="#111" stroke-width="1.3"><path d="M7 17s6-6 6-10A6 6 0 0 0 1 7c0 4 6 10 6 10z"/><circle cx="7" cy="7" r="2"/></svg>
    <div style="line-height:1.6">Lorem Ipsum, 109 Street,<br>Harbourside</div>
  </div>
  <div class="contact-stack" style="width:140px;margin-left:6px">
    <svg width="16" height="12" viewBox="0 0 16 12" fill="none" stroke="#111" stroke-width="1.2"><rect x="1" y="1" width="14" height="10"/><path d="M1 1l7 6 7-6"/></svg>
    <span>info@calvanta.com</span>
  </div>
  <div class="contact-stack" style="width:140px;margin-left:20px">
    <svg width="14" height="14" viewBox="0 0 14 14" fill="none" stroke="#111" stroke-width="1.2"><path d="M3 1l2 3-1.5 1.5a8 8 0 0 0 5 5L10 9l3 2-1 2C6 13 1 8 1 2z"/></svg>
    <span>+61 200 555 014</span>
  </div>
  <div class="divider" style="margin-left:30px"></div>
  <div class="social" style="margin-left:32px;gap:14px"><span style="width:18px;height:18px;background:#888"></span><span style="width:18px;height:18px;background:#888"></span><span style="width:18px;height:18px;background:#888"></span></div>
</div>
<nav class="abs footer-nav"><span>Home</span><i>/</i><span>About Us</span><i>/</i><span>Work</span><i>/</i><span>Contact Us</span></nav>
<div class="abs copyright">Copyright © 2020 Calvanta. All Rights Reserved</div>

</body>
</html>
```